Trade fair PLAMX business card 7” x 5”

PLAMX exhibits on technology-hospitality trade fair in the UK this year. Therefore we are looking for well-designed marketing card (examples are linked in the bottom). The main role of these materials is to attract receivers to visit our website & find out more about PLAMX solutions.
Preferred used colours: white, various blue tints, black.
The front should contain branding & motto (“Modern beverage stocktaking”). Logotypes are attached.
The back should contain:
(value proposition),
Modern technology solution for beverage stocktaking
Accurate & effective stocktaking
Swift measuring with 99% accuracy makes stocktaking significantly quicker and more cost effective (or cost optimising).
Software solution supported with/by hardware tools
PLAMX system is based on universally accessible platforms - smartphones, PCs, and laptops. Your main measuring tool, smart scale, is delivered by PLAMX.
Smart & simple reporting system
Data availability - everywhere, anytime
Useful functions help stock managing at your bar
(call to action),
Find us on plamx-vend.com and try PLAMX with a one-month free trial.
(promo code)
Claim your 50% off discount with above promo code
Marketing card examples:
https://www.vendrilosa.com/Which-startup-has-the-best-brochure-in-terms-of-design-and-content
PLAMX solution was created to help bar owners, bar managers and head bartenders to make their stocktaking process swift & accurate. Therefore, our product is targeting every business which sells portioned beverages.
Information Technology

```html
<!DOCTYPE html>
<html lang="en">
<head>
<meta charset="utf-8">
<title>PLAMX — Trade Fair Card</title>
<link href="https://fonts.googleapis.com/css2?family=Lato:wght@400;700;900&family=Roboto:wght@400;700&display=swap" rel="stylesheet">
<style>
  :root {
    --canvas-bg: #e8e6e2;
    --ink-dark: #14161b;
    --ink-night: #1d2028;
    --brand-blue: #0f4f9e;
    --brand-blue-soft: rgba(15, 79, 158, 0);
    --accent-teal: #1bb39b;
    --text-white: #ffffff;
    --text-muted: #c9ced6;
    --photo-grey-light: #e4e4e4;
    --photo-grey-mid: #8c8c8c;
  }
  * { box-sizing: border-box; margin: 0; padding: 0; }
  html, body {
    width: 1200px; height: 800px; overflow: hidden;
    background: var(--canvas-bg);
  }
  .sheet {
    width: 1200px; height: 800px;
    display: flex; align-items: center; justify-content: center; gap: 40px;
  }
  .card {
    position: relative; width: 560px; height: 400px; overflow: hidden;
    box-shadow: 0 10px 30px rgba(0,0,0,0.18);
  }

  /* Front */
  .card-front { background: var(--ink-dark); font-family: "Roboto", sans-serif; }
  .front-photo {
    position: absolute; inset: 0;
    background:
      radial-gradient(ellipse at 22% 55%, rgba(120, 70, 140, 0.45), transparent 55%),
      radial-gradient(ellipse at 62% 35%, rgba(60, 80, 120, 0.35), transparent 50%),
      linear-gradient(180deg, #1a1b22 0%, #121318 60%, #0c0d10 100%);
  }
  .front-tagline {
    position: absolute; top: 34px; left: 0; right: 0; text-align: center;
    font-family: "Lato", sans-serif; font-size: 23px; color: var(--text-white);
  }
  .front-tagline .accent { color: var(--accent-teal); font-weight: 700; }
  .front-motto {
    position: absolute; top: 150px; left: 0; right: 0; text-align: center;
    font-weight: 700; font-size: 38px; line-height: 1.2; color: var(--text-white);
  }
  .front-url {
    position: absolute; right: 30px; bottom: 92px;
    font-size: 16px; color: var(--text-white);
  }
  .front-brand {
    position: absolute; left: 30px; bottom: 28px;
    display: flex; align-items: center; gap: 10px;
    font-family: "Roboto", sans-serif; font-weight: 700; font-size: 40px;
    color: var(--text-white); letter-spacing: -0.5px;
  }
  .front-brand .brand-square { width: 30px; height: 30px; background: var(--brand-blue); }

  /* Back */
  .card-back { background: var(--ink-night); font-family: "Lato", sans-serif; }
  .back-photo {
    position: absolute; top: 0; right: 0; width: 62%; height: 100%;
    background: linear-gradient(90deg, rgba(29,32,40,1) 0%, rgba(90,80,78,0.7) 35%, var(--photo-grey-mid) 60%, var(--photo-grey-light) 100%);
  }
  .back-heading-band {
    position: absolute; top: 50px; left: 0; width: 66%; height: 78px;
    padding: 14px 28px;
    background: linear-gradient(90deg, var(--brand-blue) 55%, var(--brand-blue-soft) 100%);
  }
  .back-heading {
    font-weight: 700; font-size: 21px; line-height: 1.25; color: var(--text-white);
  }
  .back-features {
    position: absolute; top: 150px; left: 28px; width: 280px;
    list-style: none;
  }
  .feature { margin-bottom: 12px; }
  .feature-title {
    font-weight: 700; font-size: 13px; letter-spacing: 0.3px;
    color: var(--accent-teal); text-transform: uppercase;
  }
  .feature-text { font-size: 11px; line-height: 1.4; color: var(--text-muted); margin-top: 3px; }
  .back-offer {
    position: absolute; right: 0; bottom: 44px; width: 46%; height: 92px;
    padding: 18px 22px; background: var(--accent-teal);
    color: var(--text-white); font-weight: 700; font-size: 18px; line-height: 1.3;
  }
  .back-offer .offer-figure { font-size: 22px; font-weight: 900; }
</style>
</head>
<body>
<main class="sheet">

  <section class="card card-back">
    <div class="back-photo" role="img" aria-label="Photo of a smiling man in a suit using a smartphone in front of a brick wall"></div>
    <div class="back-heading-band">
      <h2 class="back-heading">Modern Technology Solution For<br>Beverage Stocktaking</h2>
    </div>
    <ul class="back-features">
      <li class="feature">
        <h3 class="feature-title">Accurate &amp; effective stocktaking</h3>
        <p class="feature-text">Swift measuring with 99% accuracy makes stocktaking quicker and more cost effective.</p>
      </li>
      <li class="feature">
        <h3 class="feature-title">Software supported by hardware tools</h3>
        <p class="feature-text">Runs on smartphones, PCs and laptops. Your smart scale is delivered by PLAMX.</p>
      </li>
      <li class="feature">
        <h3 class="feature-title">Smart &amp; simple reporting system</h3>
        <p class="feature-text">Data available everywhere, anytime.</p>
      </li>
    </ul>
    <div class="back-offer">
      Claim your <span class="offer-figure">50%</span> off discount<br>with above promo code
    </div>
  </section>

  <section class="card card-front">
    <div class="front-photo" role="img" aria-label="Dimly lit bar with illuminated bottle shelves and a bartender"></div>
    <p class="front-tagline">Stocktaking made <span class="accent">easy</span></p>
    <h1 class="front-motto">Modern Beverage<br>Stocktaking</h1>
    <p class="front-url">https://plamx-vend.com</p>
    <div class="front-brand"><span class="brand-square"></span>plamx</div>
  </section>

</main>
</body>
</html>
```